Handout for attendees of educational seminar

I provide educational workshops on how to give technical presentations at conferences to scientists and engineers. My company is called Frame Your Research (www.FrameYourResearch.example). I would like a double sided, half page size flyer that can be used as a handout for attendees of my workshops. On one side of the flyer, they will get top tips for creating their next presentation. On the other side, they will get my photo, bio, and contact information. I have uploaded a draft of a full page design I made myself. I'd like the copy of the tips to remain the same, but everything else is flexible.

Target Market(s)

scientists, engineers, technical professionals

Font styles to use
Serif
Sans Serif

Requirements
Must have
• my photo (I've provided two options to choose from depending on colors...photo on side 2 only), my logo, flyer needs to be half page in size (5.5" x 8.5"), needs to be double sided, One side has the "tips" and the other side has my personal details (see attached page for copy).
Nice to have
• I like the use of icons on the "tips" side of the flyer.

```html
<!DOCTYPE html>
<html lang="en">
<head>
<meta charset="utf-8">
<title>Frame Your Research – Workshop Handout</title>
<link rel="stylesheet" href="https://fonts.googleapis.com/css2?family=Questrial&family=Montserrat:wght@800&family=Bebas+Neue&family=Oswald:wght@300&family=Source+Sans+3:ital,wght@0,400;0,600;0,700;1,400&display=swap">
<style>
:root{
  --stage:#5d5d5d;
  --green:#8db25b;
  --blue:#2f93bf;
  --dark:#2e2e2e;
  --ink:#2b2b2b;
  --white:#ffffff;
  --mark-grey:#4a4a4a;
}
*{box-sizing:border-box;margin:0;padding:0}
html,body{width:1200px;height:1200px;overflow:hidden}
body{background:radial-gradient(circle at 50% 50%,#7a7a7a,var(--stage) 70%);font-family:"Source Sans 3",sans-serif;position:relative}
.card{position:absolute;width:914px;height:591px;transform:scale(.8);transform-origin:0 0;background:var(--white);overflow:hidden;box-shadow:0 2px 6px rgba(0,0,0,.3)}
.card--tips{left:158px;top:97px}
.card--bio{left:311px;top:635px}
.card svg.shapes{position:absolute;left:0;top:0}
.abs{position:absolute}
.brand{text-align:center}
.brand__mark{display:block;margin:0 auto;width:100px;height:100px;border-radius:50%;background:var(--mark-grey)}
.brand__name{font-family:"Questrial",sans-serif;font-size:35px;color:var(--green);line-height:1;margin-top:6px;white-space:nowrap}
.brand__tag{font-family:"Questrial",sans-serif;font-size:12px;line-height:14px;letter-spacing:5px;color:var(--blue);margin-top:0;white-space:nowrap}
.tips__kicker{font-family:"Questrial",sans-serif;font-size:23px;color:var(--white);text-align:center;width:448px;left:0;top:80px}
.tips__title{font-family:"Montserrat",sans-serif;font-weight:800;font-size:56px;color:var(--ink);text-align:center;width:448px;left:0;top:100px;letter-spacing:-1px}
.tips__tagline{font-weight:600;font-size:16.5px;color:var(--white);text-align:center;width:448px;left:0;top:156px}
.tip{left:78px;width:380px;color:var(--white)}
.tip h3{font-weight:700;font-size:16.5px;line-height:1.1;color:var(--white)}
.tip p{font-size:11px;line-height:14.5px;margin-top:1px;text-align:justify}
.tip p + p{margin-top:6px}
.tip b{font-weight:700}
.tip-icon{left:25px;width:46px;height:46px}
.tips__help{left:27px;top:475px;width:460px;font-weight:700;font-size:13.5px;line-height:18px;color:var(--white)}
.tips__help span{color:var(--ink)}
.contact{font-size:14px;color:var(--white);display:flex;align-items:center;gap:6px;white-space:nowrap}
.contact svg{flex:none}
.bio__headline{left:464px;top:108px;width:430px;color:var(--ink);line-height:1;white-space:nowrap;font-weight:400}
.bio__headline .l1{display:block;font-family:"Bebas Neue",sans-serif;font-size:43px;letter-spacing:-.3px}
.bio__headline .l2{display:block;font-family:"Oswald",sans-serif;font-weight:300;font-size:35px;margin-top:-2px}
.bio__meet{left:466px;top:190px;font-family:"Questrial",sans-serif;font-size:27px;color:var(--white)}
.bio__text{left:464px;top:228px;width:421px;color:var(--white);font-style:italic;font-size:12.4px;line-height:16.2px;text-align:justify}
.bio__text p + p{margin-top:5px}
</style>
</head>
<body>

<!-- Side 1: Quick tips -->
<section class="card card--tips">
  <svg class="shapes" width="914" height="591" viewBox="0 0 914 591">
    <defs>
      <linearGradient id="stageGlow" x1="0" y1="0" x2="0" y2="1">
        <stop offset="0" stop-color="#1c1430"/>
        <stop offset=".45" stop-color="#5a2a7a"/>
        <stop offset=".8" stop-color="#c0245a"/>
        <stop offset="1" stop-color="#2a0c18"/>
      </linearGradient>
    </defs>
    <path d="M0,175 C60,80 160,32 250,32 C350,32 440,110 522,195 C465,300 465,470 600,591 L0,591 Z" fill="var(--green)"/>
    <path d="M0,158 C60,62 160,20 250,22 C290,23 315,30 335,38" fill="none" stroke="var(--blue)" stroke-width="14"/>
    <rect x="0" y="519" width="914" height="72" fill="var(--dark)"/>
    <path d="M528,214 C600,248 760,258 914,150 L914,591 L612,591 C478,470 476,300 528,214 Z" fill="url(#stageGlow)" role="img" aria-label="Photo of the speaker presenting on a conference stage"/>
    <path d="M520,200 C462,300 464,470 598,591" fill="none" stroke="var(--blue)" stroke-width="14"/>
    <path d="M505,192 C580,228 760,242 914,95" fill="none" stroke="var(--blue)" stroke-width="14"/>
    <path d="M522,208 C600,242 760,252 914,130" fill="none" stroke="var(--white)" stroke-width="5"/>
  </svg>

  <div class="abs tips__kicker">Frame Your Research</div>
  <div class="abs tips__title">QUICK TIPS</div>
  <div class="abs tips__tagline">Science not communicated is science not done!</div>

  <svg class="abs tip-icon" style="top:189px" viewBox="0 0 46 46" aria-hidden="true">
    <circle cx="23" cy="23" r="21" fill="var(--white)" stroke="var(--blue)" stroke-width="2"/>
    <rect x="12" y="13" width="22" height="8" rx="1" fill="var(--green)"/>
    <g fill="var(--green)"><circle cx="14" cy="27" r="2.3"/><circle cx="20" cy="27" r="2.3"/><circle cx="26" cy="27" r="2.3"/><circle cx="32" cy="27" r="2.3"/><circle cx="17" cy="33" r="2.3"/><circle cx="23" cy="33" r="2.3"/><circle cx="29" cy="33" r="2.3"/></g>
  </svg>
  <div class="abs tip" style="top:196px">
    <h3>Be Audience Centered</h3>
    <p>Your ability to be successful as a speaker depends upon your ability to make your audience successful.</p>
    <p><b>TIP:</b> Return to "Points of Common Ground" throughout the talk that answer the question "So what?" about the scientific info. Be an interpreter!</p>
  </div>

  <svg class="abs tip-icon" style="top:283px" viewBox="0 0 46 46" aria-hidden="true">
    <circle cx="23" cy="23" r="21" fill="var(--white)" stroke="var(--blue)" stroke-width="2"/>
    <g stroke="var(--blue)" stroke-width="2" fill="none" stroke-linecap="round">
      <path d="M14,11v8M11,16l3,3 3-3M23,11v8M20,16l3,3 3-3M32,11v8M29,16l3,3 3-3"/>
      <path d="M10,23h26"/>
      <path d="M18,27v8M15,32l3,3 3-3M28,27v8M25,32l3,3 3-3"/>
    </g>
  </svg>
  <div class="abs tip" style="top:290px">
    <h3>Filter &amp; Focus</h3>
    <p>When you try to share everything, you share nothing.</p>
    <p><b>TIP:</b> Start your planning with the "view" you want your audience to have at the end of the talk. Then ask yourself "What would they need to know in order to get there?"</p>
  </div>

  <svg class="abs tip-icon" style="top:377px" viewBox="0 0 46 46" aria-hidden="true">
    <circle cx="23" cy="23" r="21" fill="var(--white)" stroke="var(--blue)" stroke-width="2"/>
    <circle cx="23" cy="23" r="12" fill="var(--green)"/>
    <path d="M12,23 C16,16 30,16 34,23 C30,30 16,30 12,23 Z" fill="var(--white)" stroke="var(--ink)" stroke-width="1.5"/>
    <circle cx="23" cy="23" r="4" fill="var(--ink)"/>
  </svg>
  <div class="abs tip" style="top:384px">
    <h3>Show Your Science</h3>
    <p>Your slides should do something for you that your words cannot. This means make your slides VISUAL not VERBAL.</p>
    <p><b>TIP:</b> NO BULLET POINTS (seriously!). Have a brief take-away messages supported by visual evidence.</p>
  </div>

  <div class="abs tips__help"><span>Need more help?</span> Check out Nora Whitfield's Frame Your Research Boot Camp training program. Includes 1:1 Coaching!</div>

  <div class="abs contact" style="left:28px;top:533px">
    <svg width="12" height="12" viewBox="0 0 12 12"><circle cx="6" cy="6" r="5" fill="none" stroke="var(--blue)" stroke-width="1.2"/><path d="M1,6h10M6,1c-3,3-3,7,0,10M6,1c3,3,3,7,0,10" fill="none" stroke="var(--blue)" stroke-width="1"/></svg>
    www.FrameYourResearch.example
  </div>
  <div class="abs contact" style="left:254px;top:533px">
    <svg width="16" height="11" viewBox="0 0 16 11"><rect width="16" height="11" fill="var(--blue)"/><path d="M0,0l8,6 8-6" fill="none" stroke="var(--white)" stroke-width="1.2"/></svg>
    nora@frameyourresearch.example
  </div>

  <div class="abs brand" style="left:511px;top:27px;width:300px">
    <span class="brand__mark"></span>
    <div class="brand__name">Nora Whitfield</div>
    <div class="brand__tag">Frame Your Research</div>
  </div>
</section>

<!-- Side 2: Meet the presenter -->
<section class="card card--bio">
  <svg class="shapes" width="914" height="591" viewBox="0 0 914 591">
    <defs>
      <linearGradient id="portraitTone" x1="0" y1="0" x2="1" y2="1">
        <stop offset="0" stop-color="#d9d2c8"/>
        <stop offset=".5" stop-color="#b48a68"/>
        <stop offset="1" stop-color="#1f7a55"/>
      </linearGradient>
    </defs>
    <path d="M400,172 C470,92 560,42 680,40 C790,38 880,92 914,152 L914,591 L300,591 C440,470 455,300 400,172 Z" fill="var(--green)"/>
    <path d="M392,166 C462,84 560,28 680,26 C790,24 880,80 914,137" fill="none" stroke="var(--blue)" stroke-width="14"/>
    <rect x="300" y="519" width="614" height="72" fill="var(--dark)"/>
    <path d="M0,120 C80,215 220,245 385,190 C440,300 425,470 285,591 L0,591 Z" fill="url(#portraitTone)" role="img" aria-label="Portrait photo of the presenter"/>
    <path d="M0,100 C80,195 220,225 395,172" fill="none" stroke="var(--blue)" stroke-width="14"/>
    <path d="M393,174 C450,300 436,470 296,591" fill="none" stroke="var(--blue)" stroke-width="14"/>
  </svg>

  <div class="abs brand" style="left:63px;top:23px;width:300px">
    <span class="brand__mark"></span>
    <div class="brand__name">Nora Whitfield</div>
    <div class="brand__tag">Frame Your Research</div>
  </div>

  <h2 class="abs bio__headline"><span class="l1">SCIENCE NOT COMMUNICATED</span><span class="l2">IS SCIENCE NOT DONE.</span></h2>
  <div class="abs bio__meet">Meet Nora</div>
  <div class="abs bio__text">
    <p>Nora Whitfield is on a mission: to transform how scientists, engineers, and technical professionals present their work. That's because she believes that even the best technical ideas are destined to remain undiscovered unless presented in a clear and compelling way that sparks innovation and drives adoption.</p>
    <p>For a decade, she's traveled around the world to work with top 100 corporations, institutions and universities, teaching the proven strategies she's mastered through her consulting work and during her time as a faculty member at Ridgefield State University.</p>
    <p>Nora is internationally known for her popular conference talk entitled "Speak Plainly to Me" which has over 2 million views (and counting!).</p>
    <p>Teams that work with Nora get the practical skills and natural confidence they need to immediately shift their "information dump"-style presentations into ones that are meaningful, engaging, and inspire people to take action.</p>
    <p>Nora provides on-site group workshops and coaching, conference sessions and keynotes, and 1:1 consultation.</p>
  </div>

  <div class="abs contact" style="left:426px;top:533px">
    <svg width="12" height="12" viewBox="0 0 12 12"><circle cx="6" cy="6" r="5" fill="none" stroke="var(--blue)" stroke-width="1.2"/><path d="M1,6h10M6,1c-3,3-3,7,0,10M6,1c3,3,3,7,0,10" fill="none" stroke="var(--blue)" stroke-width="1"/></svg>
    www.FrameYourResearch.example
  </div>
  <div class="abs contact" style="left:651px;top:533px">
    <svg width="16" height="11" viewBox="0 0 16 11"><rect width="16" height="11" fill="var(--blue)"/><path d="M0,0l8,6 8-6" fill="none" stroke="var(--white)" stroke-width="1.2"/></svg>
    nora@frameyourresearch.example
  </div>
</section>

</body>
</html>
```